Marwick Ostrand Law website for a law firm

modern clean website for a small boutique law firm. Based in Sacramento, CA and the Bay Area. Practice areas of Family Law, Civil litigation, and Criminal Defense. We already have a logo design as well as attorney pictures to include on page.
Would like images of California included on site.
Would like site to go with Logo that is already designed...blue/grey/white colors.

Industry/Entity Type

Law Firm

Number of Pages Required

5+ page

Requirements
Must have
• I already have several pages of content drafted. Just need the pages with images to input content. Must be clean and modern feel. Want it to reflect California and small boutique feel that is provided personalized legal attention.
• Must have a page where I can blog or post articles on.

```html
<!DOCTYPE html>
<html lang="en">
<head>
<meta charset="utf-8">
<title>Marwick Ostrand Law</title>
<link rel="stylesheet" href="https://fonts.googleapis.com/css2?family=Roboto:wght@400;500;700&family=Source+Sans+3:wght@400;600;700&display=swap">
<style>
:root{
  --blue:#3d7cc9;
  --ink:#1e1e1e;
  --text:#4a4a4a;
  --line:#e6e6e6;
  --white:#ffffff;
  --paper:#f1f2f3;
  --mist:#e9edf1;
}
*{box-sizing:border-box;margin:0;padding:0}
html,body{width:1200px;height:2296px;overflow:hidden}
body{font-family:"Source Sans 3",Arial,sans-serif;color:var(--text);background:var(--white);position:relative}
a{color:inherit;text-decoration:none}
.wrap{width:976px;margin:0 auto;position:relative}

/* header */
.site-header{height:68px;background:var(--white);position:relative;z-index:2}
.site-header .wrap{display:flex;align-items:center;height:68px;justify-content:space-between}
.brand{font-family:"Roboto",sans-serif;font-weight:500;font-size:22px;color:var(--ink);white-space:nowrap}
.main-nav{display:flex;align-items:center;gap:30px;font-family:"Roboto",sans-serif;font-weight:700;font-size:13px;color:var(--ink);text-transform:uppercase}
.main-nav .active{color:var(--blue)}
.main-nav .phone{color:var(--blue);display:flex;align-items:center;gap:6px;font-weight:500;font-size:14px}

/* hero */
.hero{height:514px;position:relative;background:linear-gradient(90deg,#8a6a52 0%,#5b4a44 30%,#3b3a40 50%,#7a3a2c 72%,#a8544a 100%);text-align:center;color:var(--white)}
.hero-photo{position:absolute;inset:0}
.hero-title{position:absolute;left:0;right:0;top:336px;font-family:"Roboto",sans-serif;font-weight:700;font-size:50px;text-shadow:0 2px 6px rgba(0,0,0,.35)}
.hero-sub{position:absolute;left:0;right:0;top:393px;font-size:20px;text-shadow:0 1px 4px rgba(0,0,0,.4)}
.hero-dots{position:absolute;left:0;right:0;top:484px;display:flex;justify-content:center;gap:4px}
.hero-dots span{width:12px;height:12px;border-radius:50%;border:1.5px solid var(--white)}
.hero-dots span.on{background:var(--white)}

/* practice areas */
.practice{height:459px;position:relative;background:linear-gradient(180deg,#fbf0e3 0%,#fde6c2 45%,#f3c98e 58%,#2f6fc0 70%,#1d57a9 100%)}
.practice-bg{position:absolute;inset:0}
.section-title{font-family:"Roboto",sans-serif;font-weight:500;font-size:20px;color:var(--ink);text-align:center;text-transform:uppercase}
.practice .section-title{padding-top:40px}
.practice-cards{display:flex;gap:9px;margin-top:37px}
.practice-card{width:237px;height:306px;background:var(--white);box-shadow:0 2px 8px rgba(0,0,0,.12);border-radius:2px;overflow:hidden}
.practice-img{height:170px;border-bottom:8px solid var(--blue)}
.practice-card h3{font-family:"Roboto",sans-serif;font-weight:700;font-size:15px;color:var(--ink);margin:16px 18px 8px;text-transform:uppercase}
.practice-card p{font-size:13px;line-height:19px;margin:0 18px}
.readmore{display:inline-flex;align-items:center;gap:3px;font-size:11px;font-weight:600;color:var(--blue);text-transform:uppercase;margin:12px 18px 0}

/* welcome */
.welcome{height:214px;background:var(--mist);text-align:center}
.welcome .section-title{padding-top:42px;font-weight:700}
.welcome p{width:820px;margin:12px auto 0;font-size:13px;line-height:19.5px;color:var(--text)}
.btn-outline{display:inline-block;margin-top:16px;width:135px;height:36px;line-height:33px;border:1.5px solid var(--blue);border-radius:18px;color:var(--blue);font-family:"Roboto",sans-serif;font-weight:500;font-size:12px;text-transform:uppercase;background:var(--white)}

/* attorneys */
.attorneys{height:337px;position:relative;background:linear-gradient(180deg,#dfe4e8 0%,#a8b39a 25%,#6f8a55 60%,#4e6b3c 100%)}
.attorney-row{display:flex;gap:28px;padding-top:8px}
.attorney-card{width:474px;height:286px;background:var(--white);display:flex;box-shadow:0 2px 8px rgba(0,0,0,.15)}
.attorney-photo{width:225px;height:286px;flex:none}
.attorney-body{padding:20px 26px}
.attorney-body h3{font-family:"Roboto",sans-serif;font-weight:700;font-size:15px;color:var(--ink);text-transform:uppercase;margin-bottom:10px}
.attorney-body p{font-size:13px;line-height:19px;margin-bottom:19px}
.attorney-body .readmore{margin:0}

/* blog */
.blog{height:294px;background:var(--white)}
.blog-head{display:flex;justify-content:space-between;align-items:center;padding-top:40px;padding-bottom:12px;border-bottom:4px solid var(--line)}
.blog-head h2{font-family:"Roboto",sans-serif;font-weight:700;font-size:19px;color:var(--ink);text-transform:uppercase}
.view-all{font-family:"Roboto",sans-serif;font-weight:700;font-size:12px;color:var(--blue);display:flex;align-items:center;gap:4px}
.posts{display:flex;margin-top:26px}
.post{width:334px;padding-right:24px}
.post time{font-size:10px;color:var(--ink);text-transform:uppercase;display:block}
.post h3{font-family:"Roboto",sans-serif;font-weight:500;font-size:16px;line-height:20px;color:var(--blue);margin-top:6px}
.post p{font-size:14px;line-height:19px;margin-top:8px}
.post .readmore{margin:10px 0 0}

/* cta */
.cta{height:221px;position:relative;background:linear-gradient(90deg,#2f3a40 0%,#56616a 40%,#6d6a5e 70%,#9a7c5a 100%);text-align:center;color:var(--white)}
.cta-photo{position:absolute;inset:0}
.cta-inner{position:relative;padding-top:48px}
.cta h2{font-family:"Roboto",sans-serif;font-weight:700;font-size:20px;text-transform:uppercase}
.cta p{font-size:13px;line-height:20px;margin-top:6px}
.btn-solid{display:inline-block;margin-top:12px;width:168px;height:37px;border-radius:19px;background:var(--blue);border:2px solid var(--white);color:var(--white);font-family:"Roboto",sans-serif;font-weight:700;font-size:12px;text-transform:uppercase;line-height:33px}

/* footer */
.site-footer{height:189px;background:var(--paper)}
.footer-cols{display:flex;padding-top:40px;font-size:12.5px;line-height:19px;color:var(--text)}
.footer-col h4{font-family:"Roboto",sans-serif;font-weight:700;font-size:12px;color:var(--ink);text-transform:uppercase;margin-bottom:5px}
.col-links{width:167px}.col-areas{width:176px}.col-contact{width:202px}.col-social{width:208px}
.social{display:flex;gap:4px;margin-top:8px}
.social span{width:24px;height:24px;border-radius:50%;border:1.5px solid #8c8c8c}
.footer-brand .brand{display:block;font-size:22px;line-height:30px}
.footer-brand p{margin-top:42px;font-size:12.5px;line-height:18px}
</style>
</head>
<body>

<header class="site-header">
  <div class="wrap">
    <a class="brand" href="#">Marwick Ostrand Law</a>
    <nav class="main-nav">
      <a class="active" href="#">Home</a>
      <a href="#">About Us</a>
      <a href="#">Practice Areas</a>
      <a href="#">Blog</a>
      <a href="#">Contact Us</a>
      <a class="phone" href="#"><svg width="10" height="14" viewBox="0 0 10 14"><rect x="0.5" y="0.5" width="9" height="13" rx="1.5" fill="var(--blue)"/><rect x="2" y="2" width="6" height="8" fill="#fff"/></svg>(916) 555-0142</a>
    </nav>
  </div>
</header>

<section class="hero">
  <div class="hero-photo" role="img" aria-label="Photo of the two founding attorneys standing in front of a brick office building"></div>
  <h1 class="hero-title">Marwick Ostrand Law</h1>
  <p class="hero-sub">Strong Reputations Don't Go Unnoticed.</p>
  <div class="hero-dots"><span class="on"></span><span></span><span></span><span></span><span></span></div>
</section>

<section class="practice">
  <div class="practice-bg" role="img" aria-label="Sunset sky over snowy California mountains in blue tones"></div>
  <div class="wrap">
    <h2 class="section-title">Practice Areas</h2>
    <div class="practice-cards">
      <article class="practice-card">
        <div class="practice-img" role="img" aria-label="Gavel and scales before shelves of law books" style="background:linear-gradient(135deg,#5a2e16,#b56a2c 55%,#3a1f10)"></div>
        <h3>Civil Litigation</h3>
        <p>Marwick Ostrand Law is a well respected civil litigation firm in Northern California.</p>
        <a class="readmore" href="#">Readmore <svg width="5" height="7"><path d="M0 0L5 3.5L0 7Z" fill="var(--blue)"/></svg></a>
      </article>
      <article class="practice-card">
        <div class="practice-img" role="img" aria-label="Hands sheltering paper cut-out family figures" style="background:linear-gradient(135deg,#f4f4f4,#dcdcdc 60%,#c9c9cc)"></div>
        <h3>Family Law</h3>
        <p>Marwick Ostrand Law offers a dedicated and highly skilled family law practice in Sacramento.</p>
        <a class="readmore" href="#">Readmore <svg width="5" height="7"><path d="M0 0L5 3.5L0 7Z" fill="var(--blue)"/></svg></a>
      </article>
      <article class="practice-card">
        <div class="practice-img" role="img" aria-label="Conference table with office chairs" style="background:linear-gradient(135deg,#d8d8d8,#6a5a50 50%,#2a2a2e)"></div>
        <h3>Immigration</h3>
        <p>Marwick Ostrand Law is a well-respected civil litigation firm in Northern California.</p>
        <a class="readmore" href="#">Readmore <svg width="5" height="7"><path d="M0 0L5 3.5L0 7Z" fill="var(--blue)"/></svg></a>
      </article>
      <article class="practice-card">
        <div class="practice-img" role="img" aria-label="Statue of justice holding scales in a library" style="background:linear-gradient(135deg,#2a1a12,#7a4a2a 50%,#c28a4a)"></div>
        <h3>Criminal Defense</h3>
        <p>You have the right to remain silent and you have the right to an attorney.</p>
        <a class="readmore" href="#">Readmore <svg width="5" height="7"><path d="M0 0L5 3.5L0 7Z" fill="var(--blue)"/></svg></a>
      </article>
    </div>
  </div>
</section>

<section class="welcome">
  <h2 class="section-title">Welcome to Marwick Ostrand Law</h2>
  <p>After practicing in both the private and public sector for several years, Renata Marwick and Theo Ostrand joined their legal expertise and formed Marwick Ostrand Law in 2015. With a combined 15 years of experience, Renata and Theo specialize in Civil Litigation, Family Law, Immigration and Criminal Defense. Their goal is to provide their clients with the best possible outcome in each and every case.</p>
  <a class="btn-outline" href="#">Explore More</a>
</section>

<section class="attorneys" aria-label="Attorneys">
  <div class="wrap">
    <div class="attorney-row">
      <article class="attorney-card">
        <div class="attorney-photo" role="img" aria-label="Portrait of attorney Renata T. Marwick" style="background:linear-gradient(160deg,#6d8fb0,#3a4250 55%,#c9b8a5)"></div>
        <div class="attorney-body">
          <h3>Renata T. Marwick</h3>
          <p>Marwick Ostrand Law offers a dedicated and highly skilled family law practice in Sacramento.</p>
          <p>A former prosecutor, Renata has decided to start her private practice to focus more attention on individual clients.</p>
          <a class="readmore" href="#">Readmore <svg width="5" height="7"><path d="M0 0L5 3.5L0 7Z" fill="var(--blue)"/></svg></a>
        </div>
      </article>
      <article class="attorney-card">
        <div class="attorney-photo" role="img" aria-label="Portrait of attorney Theo S. Ostrand" style="background:linear-gradient(160deg,#a0522d,#2b2b33 55%,#e8e8e8)"></div>
        <div class="attorney-body">
          <h3>Theo S. Ostrand</h3>
          <p>Theo Ostrand is a founding partner of Marwick Ostrand Law.</p>
          <p>After years of helping clients at other local civil litigation law firms, he started this firm so he could serve his clients with the care and devotion they deserve.</p>
          <a class="readmore" href="#">Readmore <svg width="5" height="7"><path d="M0 0L5 3.5L0 7Z" fill="var(--blue)"/></svg></a>
        </div>
      </article>
    </div>
  </div>
</section>

<section class="blog">
  <div class="wrap">
    <div class="blog-head">
      <h2>From the Blog</h2>
      <a class="view-all" href="#">VIEW ALL <svg width="5" height="8"><path d="M0 0L5 4L0 8Z" fill="var(--blue)"/></svg></a>
    </div>
    <div class="posts">
      <article class="post">
        <time>30 July 2017</time>
        <h3>Awesome lorem ipsum dolor sit dosis odio mauris.</h3>
        <p>Class aptent taciti asumed sociosqu ad litora torquent per conubia era nostra, per inceptos himenaeos.</p>
        <a class="readmore" href="#">Readmore <svg width="5" height="7"><path d="M0 0L5 3.5L0 7Z" fill="var(--blue)"/></svg></a>
      </article>
      <article class="post">
        <time>30 July 2017</time>
        <h3>Awesome lorem ipsum dolor sit dosis odio mauris.</h3>
        <p>Class aptent taciti asumed sociosqu ad litora torquent per conubia era nostra, per inceptos himenaeos.</p>
        <a class="readmore" href="#">Readmore <svg width="5" height="7"><path d="M0 0L5 3.5L0 7Z" fill="var(--blue)"/></svg></a>
      </article>
      <article class="post">
        <time>30 July 2017</time>
        <h3>Awesome lorem ipsum dolor sit dosis odio mauris.</h3>
        <p>Class aptent taciti asumed sociosqu ad litora torquent per conubia era nostra, per inceptos himenaeos.</p>
        <a class="readmore" href="#">Readmore <svg width="5" height="7"><path d="M0 0L5 3.5L0 7Z" fill="var(--blue)"/></svg></a>
      </article>
    </div>
  </div>
</section>

<section class="cta">
  <div class="cta-photo" role="img" aria-label="Coastal California bridge beneath rocky cliffs, darkened"></div>
  <div class="cta-inner">
    <h2>How Can We Help You?</h2>
    <p>We ready to help you. Give us a call or fill out this form to request service or ask a question about it.<br>We look forward to visiting with you!</p>
    <a class="btn-solid" href="#">Contact Us Today!</a>
  </div>
</section>

<footer class="site-footer">
  <div class="wrap footer-cols">
    <div class="footer-col col-links">
      <h4>Quick Links</h4>
      Home<br>About Us<br>Practice Areas<br>Blog<br>Contact Us
    </div>
    <div class="footer-col col-areas">
      <h4>Practice Areas</h4>
      Civil Litigation<br>Family Law<br>Immigration<br>Criminal Defense
    </div>
    <div class="footer-col col-contact">
      <h4>Contact Us</h4>
      Marwick Ostrand Law<br>418 Capitol Row, Suite 200<br>Sacramento, CA 95814<br>T: (916) 555-0142<br>E: info@marwickostrand.com
    </div>
    <div class="footer-col col-social">
      <h4>We're Social</h4>
      <div class="social"><span></span><span></span><span></span><span></span><span></span></div>
    </div>
    <div class="footer-col footer-brand">
      <span class="brand">Marwick Ostrand Law</span>
      <p>© 2017 Marwick Ostrand Law.<br>All Rights Reserved</p>
    </div>
  </div>
</footer>

</body>
</html>
```